Holistic/ Sports Psychologist needs flyer design

I need a flyer designed that catches the attention of potential customers - (parents of young athletes and athletes) who may be looking for psychological services. I have a logo and all the relevant info for the flyer but would like someone to take it and make it look creative, fun, fresh and attention getting for high school and college athletes. The colors used can be from my logo design which represents my holistic approach.
Target Market(s)
high school and collegiate athletes
Industry/Entity Type
sports psychology
Requirements
Must have
- Info I put on the flyer with my logo and please add some graphics and color based on my logo

```html
<!DOCTYPE html>
<html lang="en">
<head>
<meta charset="utf-8">
<title>Holistic and Sports Psychology Flyer</title>
<link href="https://fonts.googleapis.com/css2?family=Poppins:wght@400;500;600;700&display=swap" rel="stylesheet">
<style>
:root{
  --bg:#aeb0c8;
  --blue:#3a6ea5;
  --navy:#1f4f8a;
  --title:#2f5f99;
  --green:#a9d47a;
  --ink:#1d1d1d;
  --white:#ffffff;
}
*{box-sizing:border-box;margin:0;padding:0}
html,body{width:1200px;height:1200px;overflow:hidden}
body{background:var(--bg);font-family:'Poppins',sans-serif;color:var(--ink);position:relative}
.page{position:absolute;top:222px;width:491px;height:694px;background:var(--white);overflow:hidden}
.page--front{left:92px}
.page--back{left:617px}
.header-shape{position:absolute;left:0;top:0;width:491px;height:340px}
.hero{position:absolute;left:112px;top:40px;width:266px;height:266px;border-radius:50%}
.hero--beach{background:linear-gradient(180deg,#a9cde8 0%,#3f86a8 100%)}
.hero--hands{background:radial-gradient(circle at 50% 55%,#b9a9e0 0%,#6a5bb8 40%,#24358f 100%)}
.badge{position:absolute;border-radius:50%;border:3px solid var(--navy);background:var(--white)}
.badge--brand{left:322px;top:209px;width:126px;height:126px;display:flex;flex-direction:column;align-items:center;justify-content:center;gap:6px}
.brand-dot{width:44px;height:44px;border-radius:50%;background:var(--green)}
.brand-name{font-size:10px;font-weight:500;color:var(--title);text-align:center;line-height:1.2;padding:0 6px}
.badge--portrait{left:292px;top:208px;width:162px;height:162px;border:3px solid var(--white);background:linear-gradient(160deg,#d8dbe0,#9aa2ad 60%,#c9b48a)}
.title{position:absolute;left:0;width:100%;text-align:center;color:var(--title);font-weight:600;font-size:23px;line-height:29px;top:338px}
.subtitle-band{position:absolute;left:0;top:401px;width:100%;height:50px;background:var(--green);color:var(--white);text-align:center;font-size:15px;font-weight:500;line-height:21px;padding-top:4px}
.subtitle-band::after{content:"";position:absolute;left:239px;bottom:-9px;border-left:9px solid transparent;border-right:9px solid transparent;border-top:9px solid var(--green)}
.services{position:absolute;top:467px;left:0;width:100%;height:190px}
.col{position:absolute;top:0}
.col--left{left:12px;width:222px}
.col--right{left:250px;width:228px;border-left:1px solid #c9c9c9;padding-left:10px;height:180px}
.service{display:flex;gap:6px;margin-bottom:12px}
.service-icon{flex:0 0 26px;height:26px;border-radius:50%;background:var(--green);opacity:.7;margin-top:2px}
.service h3{font-size:12.5px;font-weight:600;color:var(--title);line-height:16px}
.service p{font-size:8.3px;line-height:12px;margin-top:2px}
.footer{position:absolute;left:0;bottom:0;width:100%;height:30px;background:var(--blue);color:var(--white);display:flex;align-items:center;justify-content:center;font-size:10.5px;font-weight:600;gap:10px}
.footer .divider{width:1px;height:16px;background:rgba(255,255,255,.6)}
.footer .phone{display:flex;align-items:center;gap:4px}
.pill{position:absolute;left:0;background:var(--navy);color:var(--white);font-weight:600;border-radius:0 16px 16px 0;display:flex;align-items:center;padding-left:24px;box-shadow:3px 3px 5px rgba(0,0,0,.25)}
.pill--about{top:329px;width:144px;height:30px;font-size:18px}
.pill--spec{top:470px;width:311px;height:32px;font-size:18.5px;padding-left:22px}
.about-text{position:absolute;left:24px;top:372px;width:256px;font-size:8.2px;line-height:13.5px}
.doctor-name{position:absolute;left:327px;top:388px;font-size:14px;font-weight:600;line-height:18px}
.spec-list{position:absolute;top:517px;list-style:none;font-size:10px;line-height:18.5px}
.spec-list--a{left:24px}
.spec-list--b{left:174px;border-left:1px solid #c9c9c9;padding-left:10px;top:513px;line-height:22px;height:92px}
.spec-list li{display:flex;align-items:center;gap:8px}
.spec-list svg{flex:0 0 10px}
.telehealth{position:absolute;left:344px;top:441px;width:147px;height:178px;background:linear-gradient(180deg,var(--navy),var(--blue));border-radius:18px 0 0 18px;color:var(--white);font-size:14px;line-height:22px;padding:22px 0 0 15px;white-space:nowrap}
.telehealth strong{font-weight:700}
.address{position:absolute;left:0;top:633px;width:100%;text-align:center;font-size:14px;font-weight:500;display:flex;justify-content:center;align-items:center;gap:6px}
</style>
</head>
<body>

<section class="page page--front">
  <svg class="header-shape" viewBox="0 0 491 340" aria-hidden="true">
    <rect width="491" height="300" fill="var(--blue)"/>
    <path d="M0 10 C25 2 45 20 45 60 L45 240 C45 285 80 300 110 300 L0 300 Z" fill="var(--white)"/>
    <path d="M491 10 C466 2 446 20 446 60 L446 240 C446 285 411 300 381 300 L491 300 Z" fill="var(--white)"/>
    <path d="M90 175 A155 155 0 0 1 400 175 L365 175 A120 120 0 0 0 125 175 Z" fill="var(--green)"/>
    <path d="M90 175 A155 155 0 0 0 400 175 L365 175 A120 120 0 0 1 125 175 Z" fill="var(--navy)"/>
  </svg>
  <div class="hero hero--beach" role="img" aria-label="Photo of a woman meditating on a beach facing the sea"></div>
  <div class="badge badge--brand">
    <span class="brand-dot"></span>
    <span class="brand-name">Dr. Lorelei Ashcombe</span>
  </div>

  <h1 class="title">Holistic Psychology and<br>Sports Psychology Consulting</h1>
  <div class="subtitle-band">Ways to Improve Athletic Performance Using<br>Sports and Holistic Psychology</div>

  <div class="services">
    <div class="col col--left">
      <div class="service"><span class="service-icon" role="img" aria-label="Mind icon"></span><div><h3>Mental Skills Training</h3><p>Ex: visualization, goal-setting, motivation, self- talk, mindset, concentration techniques</p></div></div>
      <div class="service"><span class="service-icon" role="img" aria-label="Growth chart icon"></span><div><h3>Performance Enhancement</h3><p>Eliminate psychological barriers that are hindering performance such as self- doubt, perfectionism, fear of failure, and burnout</p></div></div>
      <div class="service"><span class="service-icon" role="img" aria-label="Mental health icon"></span><div><h3>Mental Health</h3><p>Anxiety and stress management by using relaxation techniques, breathwork, and mindfulness practices</p></div></div>
    </div>
    <div class="col col--right">
      <div class="service"><span class="service-icon" role="img" aria-label="Recovery icon"></span><div><h3>Injury Recovery Support</h3><p>Assist athletes in maintaining resilience and positive mental attitude during rehabilitation as well as processing emotions relating to any potential trauma caused by the injury or life transitions resulting from it.</p></div></div>
      <div class="service"><span class="service-icon" role="img" aria-label="Balance icon"></span><div><h3>Burnout prevention</h3><p>Teach athletes how to have balance in sports and life so they can experience longevity in their sports as well as overall optimal health and well-being.</p></div></div>
    </div>
  </div>

  <footer class="footer">
    <span>www.drlorelei-example.com</span><span class="divider"></span>
    <span class="phone"><svg width="13" height="13" viewBox="0 0 16 16"><circle cx="8" cy="8" r="8" fill="#fff"/><path d="M5 4.2l1.6 0 .7 2-1 .8c.5 1.1 1.2 1.8 2.3 2.3l.8-1 2 .7v1.6c0 .5-.4.8-.9.8C7.4 11.2 4.8 8.6 4.2 5.1c0-.5.3-.9.8-.9z" fill="var(--blue)"/></svg>555-210-4870</span>
  </footer>
</section>

<section class="page page--back">
  <svg class="header-shape" viewBox="0 0 491 340" aria-hidden="true">
    <rect width="491" height="300" fill="var(--blue)"/>
    <path d="M0 10 C25 2 45 20 45 60 L45 240 C45 285 80 300 110 300 L0 300 Z" fill="var(--white)"/>
    <path d="M491 10 C466 2 446 20 446 60 L446 240 C446 285 411 300 381 300 L491 300 Z" fill="var(--white)"/>
    <path d="M90 175 A155 155 0 0 1 400 175 L365 175 A120 120 0 0 0 125 175 Z" fill="var(--green)"/>
    <path d="M90 175 A155 155 0 0 0 400 175 L365 175 A120 120 0 0 1 125 175 Z" fill="var(--navy)"/>
  </svg>
  <div class="hero hero--hands" role="img" aria-label="Photo of open hands holding amethyst crystals"></div>
  <div class="badge badge--portrait" role="img" aria-label="Portrait photo of the psychologist with her dog"></div>
  <p class="doctor-name">Dr. Lorelei<br>Ashcombe</p>

  <h2 class="pill pill--about">About Us</h2>
  <p class="about-text">Dr. Lorelei Ashcombe is a licensed psychologist. She understands the unique experiences of athletes due to her background as an All-American swimmer, collegiate and age group swim coach, parent of a collegiate/professional athlete, and sports psychology researcher. She works with athletes to optimize performance and overall well-being.</p>

  <h2 class="pill pill--spec">Her specializations include:</h2>
  <ul class="spec-list spec-list--a">
    <li><svg width="10" height="10" viewBox="0 0 10 10"><circle cx="5" cy="5" r="5" fill="var(--ink)"/><path d="M4 3l2 2-2 2" stroke="#fff" stroke-width="1.2" fill="none"/></svg>Performance anxiety</li>
    <li><svg width="10" height="10" viewBox="0 0 10 10"><circle cx="5" cy="5" r="5" fill="var(--ink)"/><path d="M4 3l2 2-2 2" stroke="#fff" stroke-width="1.2" fill="none"/></svg>Mental performance</li>
    <li><svg width="10" height="10" viewBox="0 0 10 10"><circle cx="5" cy="5" r="5" fill="var(--ink)"/><path d="M4 3l2 2-2 2" stroke="#fff" stroke-width="1.2" fill="none"/></svg>Stress management</li>
    <li><svg width="10" height="10" viewBox="0 0 10 10"><circle cx="5" cy="5" r="5" fill="var(--ink)"/><path d="M4 3l2 2-2 2" stroke="#fff" stroke-width="1.2" fill="none"/></svg>Anxiety</li>
    <li><svg width="10" height="10" viewBox="0 0 10 10"><circle cx="5" cy="5" r="5" fill="var(--ink)"/><path d="M4 3l2 2-2 2" stroke="#fff" stroke-width="1.2" fill="none"/></svg>Depressions</li>
  </ul>
  <ul class="spec-list spec-list--b">
    <li><svg width="10" height="10" viewBox="0 0 10 10"><circle cx="5" cy="5" r="5" fill="var(--ink)"/><path d="M4 3l2 2-2 2" stroke="#fff" stroke-width="1.2" fill="none"/></svg>Trauma</li>
    <li><svg width="10" height="10" viewBox="0 0 10 10"><circle cx="5" cy="5" r="5" fill="var(--ink)"/><path d="M4 3l2 2-2 2" stroke="#fff" stroke-width="1.2" fill="none"/></svg>Life transitions</li>
    <li><svg width="10" height="10" viewBox="0 0 10 10"><circle cx="5" cy="5" r="5" fill="var(--ink)"/><path d="M4 3l2 2-2 2" stroke="#fff" stroke-width="1.2" fill="none"/></svg>Relationship issues</li>
    <li><svg width="10" height="10" viewBox="0 0 10 10"><circle cx="5" cy="5" r="5" fill="var(--ink)"/><path d="M4 3l2 2-2 2" stroke="#fff" stroke-width="1.2" fill="none"/></svg>Injury, and sleep.</li>
  </ul>

  <div class="telehealth">All services<br>are provided<br>online via<br><strong>telehealth<br>Sessions</strong> are<br><strong>30</strong> or <strong>55</strong> minutes.</div>

  <p class="address"><svg width="16" height="18" viewBox="0 0 16 18"><path d="M8 1a6 6 0 0 0-6 6c0 4.5 6 10 6 10s6-5.5 6-10a6 6 0 0 0-6-6z" fill="none" stroke="var(--ink)" stroke-width="2"/><circle cx="8" cy="7" r="2.2" fill="var(--ink)"/></svg>820 Harbor Lane #110, Seabrook Cove, FL 32099</p>

  <footer class="footer">
    <span>www.drlorelei-example.com</span><span class="divider"></span>
    <span class="phone"><svg width="13" height="13" viewBox="0 0 16 16"><circle cx="8" cy="8" r="8" fill="#fff"/><path d="M5 4.2l1.6 0 .7 2-1 .8c.5 1.1 1.2 1.8 2.3 2.3l.8-1 2 .7v1.6c0 .5-.4.8-.9.8C7.4 11.2 4.8 8.6 4.2 5.1c0-.5.3-.9.8-.9z" fill="var(--blue)"/></svg>555-210-4870</span>
  </footer>
</section>

</body>
</html>
```